Hey Lunacraft, this time I go to you in direct demand :)
We need a Facebook Event Cover (High definition) :
- Name of the party "VELVET ATTIC"
- Date of the party "Samedi 25 novembre"
- Place of the party "Pivot9" (use logo please)
- DJ's: "K-Malt + RN"
- Style of the flyer : Vintage
- Inspiration : Old vintage Ads, old vintage objects linked to music, inspiration on google images "Vintage party" "Retro Vintage party", should be really stylish :)
- Colors : You decide, you can try, pastel colors ?

```html
<!DOCTYPE html>
<html lang="fr">
<head>
<meta charset="utf-8">
<title>Velvet Attic — Samedi 25 Nov</title>
<link rel="stylesheet" href="https://fonts.googleapis.com/css2?family=Monoton&display=swap">
<style>
  :root {
    --teal: #6cc0b2;
    --teal-deep: #3f9c8f;
    --teal-light: #9bd8cc;
    --pink: #f2958c;
    --pink-soft: #f6b3aa;
    --ice: #acdcd6;
    --white: #fbf7f2;
    --ink: #1e1f1d;
    --sign: #3b3b37;
    --sign-edge: #c8a29b;
  }
  * { margin: 0; padding: 0; box-sizing: border-box; }
  html, body { width: 1200px; height: 675px; overflow: hidden; }
  body { background: var(--teal); }
  .cover {
    position: relative;
    width: 1200px;
    height: 675px;
    overflow: hidden;
    background: radial-gradient(ellipse at 55% 75%, var(--teal-light) 0%, var(--teal) 45%, var(--teal-deep) 100%);
    font-family: "Monoton", cursive;
  }
  .sign { position: absolute; left: 0; top: 0; width: 560px; height: 345px; }

  .event-title {
    position: absolute;
    left: 0;
    top: 0;
    width: 560px;
    height: 340px;
    font-weight: 400;
    transform: rotate(-3deg);
    transform-origin: 60px 180px;
  }
  .event-title span {
    position: absolute;
    left: 60px;
    display: block;
    font-size: 80px;
    line-height: 1;
    white-space: nowrap;
    transform: scaleY(1.4);
    transform-origin: top left;
    text-shadow: 4px 3px 0 var(--ink);
  }
  .event-title .line-one { top: 52px; color: var(--pink); }
  .event-title .line-two { top: 172px; color: var(--ice); }

  .radio-art {
    position: absolute;
    left: 348px;
    top: 250px;
    width: 486px;
    height: 440px;
    border-radius: 46px;
    background: linear-gradient(160deg, var(--pink-soft) 0%, #cfe9e3 35%, #d89c8f 70%, var(--teal-deep) 100%);
    transform: rotate(3deg);
  }

  .date {
    position: absolute;
    left: 0;
    top: 0;
    width: 990px;
    height: 260px;
  }
  .date span {
    position: absolute;
    left: 672px;
    display: block;
    line-height: 1;
    white-space: nowrap;
    transform-origin: top left;
    text-shadow: 4px 3px 0 var(--ink);
  }
  .date .day {
    top: 40px;
    color: var(--white);
    font-size: 62px;
    transform: scaleY(1.55);
  }
  .date .when {
    top: 146px;
    color: var(--pink);
    font-size: 66px;
    letter-spacing: -1px;
    transform: scaleY(1.6);
  }

  .divider {
    position: absolute;
    left: 1000px;
    top: 70px;
    width: 2px;
    height: 172px;
    background: var(--ink);
  }

  .venue {
    position: absolute;
    left: 1016px;
    top: 118px;
    width: 160px;
    display: flex;
    flex-direction: column;
    align-items: center;
    gap: 12px;
  }
  .venue-mark {
    width: 26px;
    height: 26px;
    border-radius: 50%;
    background: var(--white);
  }
  .venue-name {
    color: var(--white);
    font-size: 28px;
    line-height: 1;
    white-space: nowrap;
  }

  .lineup {
    position: absolute;
    left: 822px;
    top: 328px;
    width: 352px;
    height: 78px;
    background: var(--pink);
    border: 3px solid var(--ink);
    border-radius: 6px;
    box-shadow: 4px 4px 0 var(--ink);
    display: flex;
    align-items: center;
    justify-content: center;
    color: var(--ink);
    font-size: 38px;
    white-space: nowrap;
  }
</style>
</head>
<body>
  <main class="cover">
    <svg class="sign" viewBox="0 0 560 345" aria-hidden="true">
      <polygon points="0,62 402,28 544,150 437,312 0,331" fill="var(--sign)" stroke="var(--sign-edge)" stroke-width="6"/>
    </svg>
    <h1 class="event-title">
      <span class="line-one">VELVET</span>
      <span class="line-two">ATTIC</span>
    </h1>
    <div class="radio-art" role="img" aria-label="Pastel pink and turquoise vintage radio with speaker grille and two dials"></div>
    <p class="date">
      <span class="day">SAMEDI</span>
      <span class="when">25 NOV</span>
    </p>
    <div class="divider"></div>
    <div class="venue">
      <span class="venue-mark"></span>
      <span class="venue-name">PIVOT9</span>
    </div>
    <p class="lineup">K-MALT + RN</p>
  </main>
</body>
</html>
```